1 page marketing brochure for subcontractor services for Florida's Petroleum Contamination cleanup

I need a marketing brochure that can be emailed to potential clients to offer our comprehensive service capabilities to Agency Term Contractors in the Coastal Bureau of Habitat Stewardship's (CBHS) Fuel Recovery Initiative. We offer turnkey support from project management, monitoring, reporting, soil and groundwater assessment, remediation system engineering, design, construction, and system rental. We would like to see designs that use the green and goldish colors in our logo. I have attached the icon from our logo and an amateur in-house created design with some key points that are important to us. The icons used as bullet points can change. I've added examples of industry correct drilling icons. I also added a second picture of a system trailer in use. We are open to different Fonts and are open to assistance with copy refinement. This single page flyer is intended only for digital use (email/website) at this time.
Updates

Target Market(s)

Agency Term contractors in Coastal Bureau of Habitat Stewardship Fuel Recovery Initiative

Industry/Entity Type

Petroleum cleanup in Florida

Requirements
Should not have
• Don't show the Brimor name in the photo. See attached examples of industry appropriate drilling icons

```html
<!DOCTYPE html>
<html lang="en">
<head>
<meta charset="utf-8">
<title>CBHS Fuel Recovery Initiative – Turnkey Support Brochure</title>
<link rel="stylesheet" href="https://fonts.googleapis.com/css2?family=Arimo:wght@400;700&display=swap">
<style>
  :root {
    --green: #2b5f3c;
    --green-deep: #245a37;
    --gold: #c8aa63;
    --gold-soft: #d6bf7d;
    --ink: #333a36;
    --paper: #fbfbfa;
    --white: #ffffff;
  }
  * { margin: 0; padding: 0; box-sizing: border-box; }
  html, body { width: 1200px; height: 1200px; overflow: hidden; }
  body { font-family: "Arimo", Arial, sans-serif; background: var(--paper); }

  .brochure { position: relative; width: 1200px; height: 1200px; display: flex; }

  /* Left column */
  .intro { position: relative; width: 649px; height: 100%; background: var(--paper); }
  .brand { position: absolute; left: 68px; top: 130px; display: flex; align-items: center; gap: 14px; }
  .brand-dot { width: 46px; height: 46px; border-radius: 50%; background: var(--green); }
  .brand-name { font-size: 30px; font-weight: 700; color: var(--green); }

  .headline { position: absolute; left: 66px; top: 290px; font-size: 42px; line-height: 53px; font-weight: 700; color: var(--green); }
  .rule { position: absolute; left: 66px; top: 490px; width: 522px; height: 3px; background: var(--gold); }
  .offer { position: absolute; left: 66px; top: 528px; font-size: 24px; line-height: 35px; color: var(--green); }

  .services { position: absolute; left: 66px; top: 694px; list-style: none; width: 540px; }
  .services li { position: relative; padding-left: 54px; font-size: 22.5px; line-height: 34px; color: var(--ink); margin-bottom: 32px; }
  .services li::before { content: ""; position: absolute; left: 2px; top: 10px; width: 16px; height: 16px; background: var(--green); transform: scaleX(1.5) rotate(45deg); }
  .services li:nth-child(2) { margin-bottom: 48px; }

  .tagline { position: absolute; left: 66px; top: 1045px; font-size: 34px; color: var(--green); }

  /* Right column */
  .capabilities { position: relative; width: 551px; height: 100%; background: var(--green-deep); }
  .site-photo { position: absolute; left: 0; top: 0; width: 551px; height: 440px; }

  .cap-title { position: absolute; left: 55px; top: 488px; font-size: 36px; line-height: 47px; font-weight: 700; color: var(--gold-soft); }
  .cap-summary { position: absolute; left: 55px; top: 612px; font-size: 20.5px; line-height: 31px; color: var(--white); }

  .cap-list { position: absolute; left: 58px; top: 774px; list-style: none; }
  .cap-list li { display: flex; align-items: center; height: 66px; margin-bottom: 26px; }
  .cap-icon { width: 66px; height: 66px; border-radius: 50%; background: var(--white); display: flex; align-items: center; justify-content: center; flex-shrink: 0; }
  .cap-text { margin-left: 22px; font-size: 20.5px; line-height: 29px; color: var(--white); }
  .cap-text.strong { font-weight: 700; }

  .closing { position: absolute; left: 55px; top: 1058px; font-size: 21px; line-height: 33px; color: var(--white); }
</style>
</head>
<body>
<main class="brochure">
  <section class="intro">
    <div class="brand">
      <span class="brand-dot"></span>
      <span class="brand-name">Halvern Environmental</span>
    </div>

    <h1 class="headline">Complete<br>Comprehensive<br>Restoration Program</h1>
    <div class="rule"></div>

    <p class="offer">Offering Turnkey Support to<br>Coastal Bureau of Habitat Stewardship<br>(CBHS) Fuel Recovery Initiative</p>

    <ul class="services">
      <li>Project management, monitoring,<br>reporting and field coordination,<br>soil and groundwater assessment</li>
      <li>Remediation system engineering,<br>design and construction,<br>system rental</li>
      <li>Agency term contractor support<br>for your project portfolio</li>
    </ul>

    <p class="tagline">CBHS Recovery Partner</p>
  </section>

  <section class="capabilities">
    <svg class="site-photo" viewBox="0 0 551 440" role="img" aria-label="Photo of a white remediation system trailer parked on a red clay site under a blue sky">
      <defs>
        <linearGradient id="siteTones" x1="0" y1="0" x2="0" y2="1">
          <stop offset="0" stop-color="#3f6fae"/>
          <stop offset="0.35" stop-color="#9cb8d6"/>
          <stop offset="0.55" stop-color="#5d7a45"/>
          <stop offset="0.75" stop-color="#c67a55"/>
          <stop offset="1" stop-color="#9a9a98"/>
        </linearGradient>
      </defs>
      <path d="M0 0 H551 V400 C470 370 380 360 300 395 C220 430 120 445 0 322 Z" fill="url(#siteTones)"/>
      <path d="M0 322 C120 445 220 430 300 395 C380 360 470 370 551 412" fill="none" stroke="#c8aa63" stroke-width="6"/>
    </svg>

    <h2 class="cap-title">Three Turnkey<br>Service Capabilities</h2>
    <p class="cap-summary">Project management, procurement,<br>field monitoring, reporting and<br>agency restoration program<br>closure coordination</p>

    <ul class="cap-list">
      <li>
        <span class="cap-icon">
          <svg width="40" height="40" viewBox="0 0 40 40" aria-hidden="true"><rect x="18" y="4" width="4" height="22" fill="#2b5f3c"/><rect x="13" y="4" width="14" height="4" fill="#2b5f3c"/><path d="M6 34 L14 24 H26 L34 34 Z" fill="#2b5f3c"/></svg>
        </span>
        <span class="cap-text">Site assessment and<br>soil boring</span>
      </li>
      <li>
        <span class="cap-icon">
          <svg width="40" height="40" viewBox="0 0 40 40" aria-hidden="true"><path d="M8 30 Q12 22 22 24 L30 12 L33 14 L26 27 Q28 32 22 33 H10 Z" fill="#2b5f3c"/><rect x="29" y="6" width="6" height="6" fill="#2b5f3c"/></svg>
        </span>
        <span class="cap-text">Groundwater sampling and<br>system rental</span>
      </li>
      <li>
        <span class="cap-icon">
          <svg width="40" height="40" viewBox="0 0 40 40" aria-hidden="true"><rect x="17" y="5" width="5" height="16" fill="#2b5f3c"/><rect x="12" y="5" width="14" height="4" fill="#2b5f3c"/><path d="M12 21 H28 L30 30 H10 Z" fill="#2b5f3c"/><rect x="9" y="31" width="22" height="3" fill="#2b5f3c"/></svg>
        </span>
        <span class="cap-text strong">Soil Removal</span>
      </li>
    </ul>

    <p class="closing">A single partner from first site visit<br>through final closure and reporting.</p>
  </section>
</main>
</body>
</html>
```